Wenna's Atelier, Beauty & Therapy. New business in Verbier, Switzerland

Simple Flyer to put in evidence a particular service that the studio offers that is
EMS ( ELECTRIC MUSCLE STIMULATION)
There is a bike festival in Verbier ion the 12th of August and i would like to take an opportunity of this slot to advertise our new suit of EMS that can be very helpful for bike riders. The product is a suit with muscle electrostimulation, And there are many advantages and functionnality. For sportsmen and women, it can
I don't have any particular picture be cause the product is very new.
But i can send you some images for you to understand what it is, but if you find some images on the web it is better :)
I upload different versions of Logo, PLEASE FEEL FREE TO CHOOSE WHAT IS BEST :)
please check this link for more information about the product applied for bikers
https://www.pulvaro-suits.example/en/cycling-training-with-muscle-electrostimulation/
Updates
Hello Designers,
Here are a few details concerning the project;
- Wenna's Atelier is not a reseller of the EMS suits, but we provide it as a service inside our studio.
- We wish to communicate on this new technology in order to bring a maximum of attention, not only for the suit, but also for the brand it self, since it is new in Verbier.
- for the flyer, i would like it to be simple, appealing, and without too much text.
- a french version of the same flyer is appreciated, without extra cost ;)
Thanks
Hello all designers,
thank you for all the good work.
For you who mentioned a date for the festival, i suggest please to take it off, and keep only " Alpen Pedal Gathering" if you want.
Thank you

```html
<!DOCTYPE html>
<html lang="en">
<head>
<meta charset="utf-8">
<title>Wenna's Atelier – EMS Flyer</title>
<link href="https://fonts.googleapis.com/css2?family=Montserrat:ital,wght@0,400;0,500;0,600;0,700;0,800;1,500;1,600&display=swap" rel="stylesheet">
<style>
  :root{
    --plum:#7b1f5e;
    --plum-dark:#5e1447;
    --pink-soft:#f4e6ef;
    --pink-mid:#e3c3d7;
    --ink:#3a2a35;
    --white:#ffffff;
  }
  *{box-sizing:border-box;margin:0;padding:0}
  html,body{width:893px;height:1200px;overflow:hidden;background:var(--white)}
  body{font-family:"Montserrat",sans-serif;color:var(--ink)}
  .flyer{position:relative;width:893px;height:1200px;overflow:hidden;background:linear-gradient(180deg,#fbf5f9 0%,#ffffff 45%,#f8eef4 100%)}
  .backdrop{position:absolute;inset:0}

  .logo-badge{position:absolute;left:20px;top:50px;width:320px;height:200px;display:flex;flex-direction:column;align-items:center;justify-content:center;text-align:center}
  .logo-dot{width:64px;height:64px;border-radius:50%;border:3px solid var(--plum);margin-bottom:12px}
  .logo-name{font-weight:600;font-size:23px;letter-spacing:3px;color:var(--plum);text-transform:uppercase;white-space:nowrap}
  .logo-tag{font-size:13px;letter-spacing:2px;color:var(--plum);margin-top:6px;font-style:italic}

  .hero-photo{position:absolute;left:415px;top:-110px;width:520px;height:520px;border-radius:50%;border:16px solid var(--plum);
    background:radial-gradient(circle at 55% 45%,#d9d6d9 0%,#b9b3b8 40%,#4a4048 75%,#2a2229 100%)}

  .intro{position:absolute;left:105px;top:365px;font-style:italic;font-weight:600;color:var(--plum);font-size:30px;line-height:1.15}
  .intro strong{display:block;font-size:32px}
  .headline{position:absolute;left:100px;top:440px;font-weight:800;font-size:170px;line-height:1;color:var(--plum);letter-spacing:-2px}
  .headline-sub{position:absolute;left:105px;top:615px;background:var(--plum);color:var(--white);font-weight:600;font-size:23px;padding:5px 18px}
  .lead{position:absolute;left:105px;top:668px;width:540px;font-size:22px;line-height:1.3;color:var(--ink)}
  .lead b{color:var(--plum);font-weight:700}
  .rule{position:absolute;left:105px;top:748px;width:200px;height:5px;background:var(--plum)}

  .benefits-title{position:absolute;left:0;top:785px;width:560px;height:46px;background:linear-gradient(90deg,var(--plum) 0%,var(--plum) 75%,rgba(123,31,94,0) 100%);color:var(--white);font-weight:700;font-size:24px;line-height:46px;padding-left:105px}

  .benefits{position:absolute;left:100px;top:852px;width:500px;display:grid;grid-template-columns:250px 250px;row-gap:14px;list-style:none}
  .benefit{display:flex;align-items:center;gap:12px;font-size:17px;font-weight:500;color:var(--ink);line-height:1.2;min-height:58px}
  .benefit-icon{flex:none;width:54px;height:54px;border-radius:50%;border:2px solid var(--plum);background:var(--white);display:flex;align-items:center;justify-content:center}

  .model-photo{position:absolute;left:600px;top:640px;width:290px;height:450px;border-radius:145px 145px 20px 20px;
    background:linear-gradient(180deg,#d8b8a4 0%,#6b5a5e 35%,#2c2529 100%)}

  .contact-bar{position:absolute;left:0;bottom:0;width:893px;height:105px;background:linear-gradient(90deg,var(--plum-dark),var(--plum));display:flex;align-items:center;padding:0 40px;color:var(--white)}
  .call{display:flex;align-items:center;gap:14px;flex:none}
  .circle-icon{width:50px;height:50px;border-radius:50%;background:var(--white);display:flex;align-items:center;justify-content:center;flex:none}
  .call-label{font-size:14px;font-weight:600;letter-spacing:1px}
  .call-number{font-size:27px;font-weight:700;letter-spacing:.5px;white-space:nowrap}
  .divider{width:2px;height:62px;background:rgba(255,255,255,.6);margin:0 28px;flex:none}
  .details{display:flex;flex-direction:column;gap:10px;font-size:14px;font-weight:500;letter-spacing:1px;white-space:nowrap}
  .detail{display:flex;align-items:center;gap:10px}
  .social{display:flex;gap:8px;margin-left:auto}
  .social span{width:22px;height:22px;border-radius:50%;background:var(--white);display:block}
</style>
</head>
<body>
<main class="flyer">
  <svg class="backdrop" width="893" height="1200" viewBox="0 0 893 1200" aria-hidden="true">
    <path d="M0 0 H470 C430 180 300 320 0 335 Z" fill="var(--white)"/>
    <path d="M0 335 C300 320 430 180 470 0" fill="none" stroke="var(--plum)" stroke-width="10"/>
    <path d="M0 352 C320 338 450 180 500 0" fill="none" stroke="var(--pink-mid)" stroke-width="4"/>
    <path d="M0 560 C200 520 420 470 893 560 V620 C500 520 250 560 0 620 Z" fill="var(--pink-soft)"/>
    <path d="M320 1095 C500 980 700 960 893 1000 V1095 Z" fill="var(--pink-soft)"/>
  </svg>

  <div class="logo-badge">
    <div class="logo-dot"></div>
    <div class="logo-name">Wenna's Atelier</div>
    <div class="logo-tag">Beauty &amp; Therapy</div>
  </div>

  <div class="hero-photo" role="img" aria-label="Athlete in an EMS training suit flexing both arms beside an EMS control unit"></div>

  <p class="intro">New Service Added to <strong>Our Studio</strong></p>
  <h1 class="headline">EMS</h1>
  <p class="headline-sub">Electric Muscle Stimulation</p>
  <p class="lead">This EMS service has many advantages and<br>functionality &amp; very helpful for <b>Bike Riders</b></p>
  <div class="rule"></div>

  <h2 class="benefits-title">Benefits of Electrostimulation</h2>
  <ul class="benefits">
    <li class="benefit"><span class="benefit-icon"><svg width="28" height="28" viewBox="0 0 30 30"><path d="M4 15h22M7 10v10M23 10v10M3 12v6M27 12v6" stroke="var(--plum)" stroke-width="2.5" fill="none" stroke-linecap="round"/></svg></span>Strength<br>Training</li>
    <li class="benefit"><span class="benefit-icon"><svg width="28" height="28" viewBox="0 0 30 30"><path d="M15 26 C4 18 3 10 9 7 c3-1 5 1 6 3 c1-2 3-4 6-3 c6 3 5 11-6 19z" stroke="var(--plum)" stroke-width="2.5" fill="none"/></svg></span>Improved<br>Circulation</li>
    <li class="benefit"><span class="benefit-icon"><svg width="28" height="28" viewBox="0 0 30 30"><path d="M15 5v20M5 15h20" stroke="var(--plum)" stroke-width="3" stroke-linecap="round"/></svg></span>Rehabilitation</li>
    <li class="benefit"><span class="benefit-icon"><svg width="28" height="28" viewBox="0 0 30 30"><path d="M4 24 L12 14 L17 19 L26 7 M20 7h6v6" stroke="var(--plum)" stroke-width="2.5" fill="none" stroke-linecap="round" stroke-linejoin="round"/></svg></span>Increased Muscular<br>Endurance</li>
    <li class="benefit"><span class="benefit-icon"><svg width="28" height="28" viewBox="0 0 30 30"><circle cx="15" cy="15" r="10" stroke="var(--plum)" stroke-width="2.5" fill="none"/><path d="M10 15l4 4 7-8" stroke="var(--plum)" stroke-width="2.5" fill="none" stroke-linecap="round"/></svg></span>Pain<br>Management</li>
    <li class="benefit"><span class="benefit-icon"><svg width="28" height="28" viewBox="0 0 30 30"><path d="M15 4 C22 12 24 16 24 19 a9 9 0 0 1-18 0 c0-3 2-7 9-15z" stroke="var(--plum)" stroke-width="2.5" fill="none"/></svg></span>Fat Loss</li>
  </ul>

  <div class="model-photo" role="img" aria-label="Woman in a black EMS suit leaning on a tablet stand"></div>

  <footer class="contact-bar">
    <div class="call">
      <span class="circle-icon"><svg width="24" height="24" viewBox="0 0 24 24"><path d="M6 3l4 1 1 5-2 1.5a12 12 0 0 0 4.5 4.5L15 13l5 1 1 4-2.5 3C10 20 4 14 3 5.5z" fill="var(--plum)"/></svg></span>
      <div><div class="call-label">CALL US TODAY</div><div class="call-number">0041 27 555 0148</div></div>
    </div>
    <div class="divider"></div>
    <div class="details">
      <div class="detail"><svg width="16" height="20" viewBox="0 0 16 20"><path d="M8 1a6.5 6.5 0 0 0-6.5 6.5C1.5 12 8 19 8 19s6.5-7 6.5-11.5A6.5 6.5 0 0 0 8 1z" fill="var(--white)"/><circle cx="8" cy="7.5" r="2.3" fill="var(--plum)"/></svg>ADDRESS/STATE/COUNTRY</div>
      <div class="detail"><svg width="16" height="16" viewBox="0 0 18 18"><circle cx="9" cy="9" r="7.5" stroke="var(--white)" stroke-width="1.6" fill="none"/><path d="M1.5 9h15M9 1.5c3 3 3 12 0 15M9 1.5c-3 3-3 12 0 15" stroke="var(--white)" stroke-width="1.3" fill="none"/></svg>WWW.WENNAS-ATELIER.EXAMPLE</div>
    </div>
    <div class="social" aria-hidden="true"><span></span><span></span><span></span></div>
  </footer>
</main>
</body>
</html>
```